Consulting company needs Business Cards - rough concept provided

I'm looking for someone to take our business card idea and make is slick and polished - to communicate our high-end, sophisticated, serious consulting business. We have a rough layout we did in-house. We are open to ideas on repo-ing elements, adjusting sizes, typefaces etc... within the general concept we've already come up with. We want it to be super-clean and sophisticated. We want to keep the white backgrounds, and blue brand colors. Our goal is to print with painted blue edges on thick cardstock. Thank you!!

```html
<!DOCTYPE html>
<html lang="en">
<head>
<meta charset="utf-8">
<title>Keenharbor business card variations</title>
<link rel="stylesheet" href="https://fonts.googleapis.com/css2?family=Archivo:wght@400;800&family=Figtree:wght@400&family=Poppins:wght@700&display=swap">
<style>
  :root {
    --page-bg: #ecf0f8;
    --brand-blue: #029ddd;
    --card-white: #ffffff;
    --ink: #111111;
    --rule-grey: #b9b9b9;
  }
  * { margin: 0; padding: 0; box-sizing: border-box; }
  html, body { width: 1200px; height: 1000px; overflow: hidden; }
  body { background: var(--page-bg); position: relative; }

  .card {
    position: absolute;
    width: 467px;
    height: 263px;
    background: var(--card-white);
    box-shadow: 3px 5px 10px rgba(40, 50, 70, 0.28);
    overflow: hidden;
  }
  .card--a { left: 76px;  top: 147px; }
  .card--b { left: 657px; top: 147px; }
  .card--c { left: 76px;  top: 589px; }
  .card--d { left: 657px; top: 589px; }

  .card__tab {
    position: absolute; left: 0; top: 0;
    width: 82px; height: 12px;
    background: var(--brand-blue);
  }
  .card__panel {
    position: absolute; left: 162px; top: 0;
    width: 305px; height: 263px;
    background: var(--brand-blue);
  }
  .card__wordmark {
    position: absolute; left: 0; top: 98px;
    width: 467px; height: 70px;
  }
  .card__wordmark text {
    font-family: "Poppins", sans-serif;
    font-weight: 700;
    font-size: 79px;
    fill: var(--ink);
  }

  .contact {
    position: absolute; left: 324px; top: 190px;
    border-left: 3px solid var(--rule-grey);
    padding-left: 5px;
    height: 58px;
    font-family: "Figtree", sans-serif;
    font-size: 10.5px;
    line-height: 12px;
    color: var(--card-white);
  }
  .contact__line { white-space: nowrap; }
  .contact__gap { margin-top: 4px; }

  .person {
    position: absolute; left: 15px;
    font-family: "Archivo", sans-serif;
    color: var(--ink);
    line-height: 1;
  }
  .person__first { font-weight: 400; display: block; }
  .person__last { font-weight: 800; display: block; }
  .person__role { font-weight: 400; color: var(--brand-blue); display: block; margin-top: 1px; }

  .card--a .person { top: 215px; }
  .card--a .person__first { font-size: 14px; }
  .card--a .person__last { font-size: 15px; letter-spacing: -0.3px; }
  .card--a .person__role { font-size: 7.4px; letter-spacing: -0.1px; }

  .card--b .person { top: 210px; }
  .card--b .person__first { font-size: 16px; }
  .card--b .person__last { font-size: 17px; }
  .card--b .person__role { font-size: 9px; letter-spacing: 0.2px; }

  .card--c .person { top: 210px; }
  .card--c .person__first { font-size: 16px; }
  .card--c .person__last { font-size: 17px; letter-spacing: -0.3px; }
  .card--c .person__role { font-size: 8.4px; letter-spacing: 0.2px; }

  .card--d .person { top: 215px; }
  .card--d .person__first { font-size: 14px; }
  .card--d .person__last { font-size: 14px; letter-spacing: 0.4px; }
  .card--d .person__role { font-size: 7.6px; letter-spacing: 0.2px; }
</style>
</head>
<body>

<div class="card card--a">
  <div class="card__tab"></div>
  <div class="card__panel"></div>
  <svg class="card__wordmark" viewBox="0 0 467 70"><text x="0" y="62" textLength="467" lengthAdjust="spacingAndGlyphs">KEENHARBOR</text></svg>
  <div class="person"><span class="person__first">DANA</span><span class="person__last">WHITLOW</span><span class="person__role">BRAND CONSULTANT</span></div>
  <div class="contact">
    <div class="contact__line">4820 Larkspur Ave, Ste 210</div>
    <div class="contact__line">Fairview, Ca 90210</div>
    <div class="contact__line contact__gap">555 201 4437</div>
    <div class="contact__line contact__gap">dana@keenharbor.com</div>
  </div>
</div>

<div class="card card--b">
  <div class="card__tab"></div>
  <div class="card__panel"></div>
  <svg class="card__wordmark" viewBox="0 0 467 70"><text x="0" y="62" textLength="467" lengthAdjust="spacingAndGlyphs">KEENHARBOR</text></svg>
  <div class="person"><span class="person__first">DANA</span><span class="person__last">WHITLOW</span><span class="person__role">BRAND CONSULTANT</span></div>
  <div class="contact">
    <div class="contact__line">4820 Larkspur Ave, Ste 210</div>
    <div class="contact__line">Fairview, Ca 90210</div>
    <div class="contact__line contact__gap">555 201 4437</div>
    <div class="contact__line contact__gap">dana@keenharbor.com</div>
  </div>
</div>

<div class="card card--c">
  <div class="card__tab"></div>
  <div class="card__panel"></div>
  <svg class="card__wordmark" viewBox="0 0 467 70"><text x="0" y="62" textLength="467" lengthAdjust="spacingAndGlyphs">KEENHARBOR</text></svg>
  <div class="person"><span class="person__first">DANA</span><span class="person__last">WHITLOW</span><span class="person__role">BRAND CONSULTANT</span></div>
  <div class="contact">
    <div class="contact__line">4820 Larkspur Ave, Ste 210</div>
    <div class="contact__line">Fairview, Ca 90210</div>
    <div class="contact__line contact__gap">555 201 4437</div>
    <div class="contact__line contact__gap">dana@keenharbor.com</div>
  </div>
</div>

<div class="card card--d">
  <div class="card__tab"></div>
  <div class="card__panel"></div>
  <svg class="card__wordmark" viewBox="0 0 467 70"><text x="0" y="62" textLength="467" lengthAdjust="spacingAndGlyphs">KEENHARBOR</text></svg>
  <div class="person"><span class="person__first">DANA</span><span class="person__last">WHITLOW</span><span class="person__role">BRAND CONSULTANT</span></div>
  <div class="contact">
    <div class="contact__line">4820 Larkspur Ave, Ste 210</div>
    <div class="contact__line">Fairview, Ca 90210</div>
    <div class="contact__line contact__gap">555 201 4437</div>
    <div class="contact__line contact__gap">dana@keenharbor.com</div>
  </div>
</div>

</body>
</html>
```